Need a sleek, professional business card design for a Web Development business

I need a unique business card designed for a web development company. It is also the parent company for any ventures I do, such as my ClipWave channel, startup ideas I have, etc. I am the single member of "Bright Harbor Code LLC." I will attach my basic logo here, so you will see the current color scheme and have the asset available. Thank you!

Target Market(s)

Startups, SMB's, Professionals

Industry/Entity Type

Business

Font styles to use
Other font styles liked:
• Lovello for headings is what I use, but not necessary.

Colors

Designer to choose colors to be used in the design.

Requirements
Nice to have
• Sleek is the word. Professional, modern, dark.
Should not have
• Any work from someone else's design. Lacking originality.

```html
<!DOCTYPE html>
<html lang="en">
<head>
<meta charset="UTF-8">
<title>Bright Harbor Code LLC – Business Card</title>
<link rel="stylesheet" href="https://fonts.googleapis.com/css2?family=Montserrat:wght@500;600&family=Arimo:wght@400;700&display=swap">
<style>
  :root {
    --bg: #121212;
    --card: #1b1b1b;
    --card-edge: #262626;
    --orange: #f5a25f;
    --coral: #f07a68;
    --pink: #e95873;
    --ghost: #222222;
    --text: #f1f1f1;
  }
  * { margin: 0; padding: 0; box-sizing: border-box; }
  html, body { width: 1200px; height: 900px; overflow: hidden; background: var(--bg); }
  .canvas {
    width: 1200px; height: 900px;
    display: flex; flex-direction: column; align-items: center; justify-content: center; gap: 40px;
  }
  .card {
    position: relative; width: 680px; height: 388px;
    background: var(--card); border: 1px solid var(--card-edge); border-radius: 6px;
    overflow: hidden; box-shadow: 0 18px 40px rgba(0,0,0,.55);
  }
  /* Contact side */
  .contact-card__info { position: absolute; left: 56px; top: 52px; font-family: "Arimo", sans-serif; z-index: 1; }
  .person-name { font-size: 30px; font-weight: 700; color: var(--text); letter-spacing: .3px; }
  .person-title { font-size: 17px; color: var(--orange); margin-top: 4px; }
  .address { margin-top: 42px; font-size: 16px; line-height: 1.45; color: var(--text); }
  .contact-list { list-style: none; margin-top: 10px; }
  .contact-list li { display: flex; align-items: center; gap: 10px; font-size: 16px; color: var(--text); height: 25px; }
  .contact-icon { width: 18px; height: 18px; border-radius: 3px; background: var(--orange); display: flex; align-items: center; justify-content: center; }
  .contact-icon svg { width: 12px; height: 12px; }
  .accent-shape { position: absolute; right: -70px; bottom: -120px; width: 380px; height: 380px; }
  /* Brand side */
  .brand-card__ghost { position: absolute; right: -90px; top: 40px; width: 360px; height: 360px; border-radius: 50%; background: var(--ghost); }
  .brand-lockup { position: absolute; left: 70px; top: 120px; display: flex; align-items: center; gap: 16px; }
  .brand-mark { width: 30px; height: 30px; border-radius: 6px; background: var(--orange); }
  .brand-name { font-family: "Montserrat", sans-serif; font-weight: 600; font-size: 34px; letter-spacing: 1px; text-transform: uppercase; color: var(--orange); white-space: nowrap; }
  .channel { position: absolute; left: 70px; top: 238px; display: flex; align-items: center; gap: 10px; font-family: "Arimo", sans-serif; font-size: 15px; color: var(--coral); }
  .channel__square { width: 18px; height: 18px; border-radius: 3px; background: var(--orange); }
  .channel__divider { width: 1px; height: 20px; background: #555; }
</style>
</head>
<body>
<main class="canvas">
  <section class="card contact-card">
    <svg class="accent-shape" viewBox="0 0 380 380" aria-hidden="true">
      <defs>
        <linearGradient id="accentGradient" x1="0" y1="0" x2="1" y2="0">
          <stop offset="0" stop-color="#f5a25f"/>
          <stop offset="0.55" stop-color="#f07a68"/>
          <stop offset="1" stop-color="#e95873"/>
        </linearGradient>
      </defs>
      <circle cx="190" cy="190" r="190" fill="url(#accentGradient)"/>
    </svg>
    <div class="contact-card__info">
      <h1 class="person-name">Marcus Hale</h1>
      <p class="person-title">Managing Director</p>
      <p class="address">418 W. Lindenfield<br>Suite 820, P.O. Box 47152</p>
      <ul class="contact-list">
        <li><span class="contact-icon"><svg viewBox="0 0 12 12"><path d="M3 1h2l1 3-1.5 1a6 6 0 0 0 2.5 2.5L8 6l3 1v2c0 1-1 2-2 2A8 8 0 0 1 1 3c0-1 1-2 2-2z" fill="#1b1b1b"/></svg></span>555.204.7781</li>
        <li><span class="contact-icon"><svg viewBox="0 0 12 12"><rect x="1" y="2.5" width="10" height="7" fill="none" stroke="#1b1b1b" stroke-width="1.4"/><path d="M1 3l5 4 5-4" fill="none" stroke="#1b1b1b" stroke-width="1.4"/></svg></span>hale@brightharborcode.com</li>
        <li><span class="contact-icon"><svg viewBox="0 0 12 12"><circle cx="6" cy="6" r="4.5" fill="none" stroke="#1b1b1b" stroke-width="1.3"/><path d="M1.5 6h9M6 1.5c-2 2.5-2 6.5 0 9M6 1.5c2 2.5 2 6.5 0 9" fill="none" stroke="#1b1b1b" stroke-width="1"/></svg></span>www.brightharborcode.com</li>
      </ul>
    </div>
  </section>

  <section class="card brand-card">
    <div class="brand-card__ghost" aria-hidden="true"></div>
    <div class="brand-lockup">
      <span class="brand-mark" aria-hidden="true"></span>
      <h2 class="brand-name">Bright Harbor Code LLC</h2>
    </div>
    <div class="channel">
      <span class="channel__square" aria-hidden="true"></span>
      <span class="channel__divider" aria-hidden="true"></span>
      <span>BrightHarborCode LLC</span>
    </div>
  </section>
</main>
</body>
</html>
```